light box menu and wall graphics

HI My name is Derek Vantolla and I am putting together a Pebble Wagons franchise. We are a high quaulity coffee offering and the retail concept is for a in-line store in a busy shopping centre food court. We are a highly visible coffee offering with vibrant bright orange colour (pantone 021 / process m60_y100)
Orange might make a good background on the menu board as it needs to blend in with colour scheme. Also the text has to be at least 15ml and not too busy but clearly legible. The font is: Akzent Rounded
The twin light boxes being used is from http://www.brightframedepot.com.au/pg/lightboxes/new/sdb/light-box-2270K.aspx
They measure in total 3m wide X .6 height

There are two elements to this job, one is the twin menu boards and the other is the wall graphic.
please see wall graphic examples attached.
This graphic is to be painted onto the wall by a sign writter.
The design to go on the wall needs to be a synonymous with our quality coffee vison and match the shop design, I have examples of the type of wall art I am after attached. I was thinking somehow a Cart with wings would look neat and we could incorportate some text into it. Such as "Coffee with Substance makes you feel good" and "Genuine Wagon" Flames could look amazing too!

My website is unfortunately down at the moment but I am attaching plenty

I have just added the menu in easy to read updated format.
Thanks to those who have expressed interest!
Updates

Hi Designers, I have just increased first prize by $100.00

Please note the signage boards run horizontally not vertically.  I have also added more artwork.

thanks

Derek

 HI there, thanks for joining.  I have just updated the brief to make it as clear as possible.

Hope you enjoy this experience.  I am here to answer any questions.

Derek

Thank you for accepting my invitation for this design job.

Look forward to seeing some designs as per brief.

Need to have this finished by Friday the 19th of October.  Thanks

Target Market(s)

Coffee lovers, kids who want hot chocolates, frappes,
etc

Industry/Entity Type

Shopping

Requirements
Must have
• Must have coffee in it for clarity.
Also in the menu any images of food or drink must be photo/posters attached

```html
<!DOCTYPE html>
<html lang="en">
<head>
<meta charset="utf-8">
<title>Menu Board</title>
<link href="https://fonts.googleapis.com/css2?family=Fredoka:wght@500;600&family=Nunito:wght@400;700;800&display=swap" rel="stylesheet">
<style>
  :root {
    --orange: #ee7d00;
    --ink: #1d1d1b;
    --white: #ffffff;
    --page: #f0f0f0;
  }
  * { margin: 0; padding: 0; box-sizing: border-box; }
  html, body { width: 1200px; height: 1000px; overflow: hidden; background: var(--page); }
  .menu-board { position: absolute; left: 28px; top: 214px; width: 1144px; height: 572px; background: var(--white); font-family: "Fredoka", sans-serif; }
  .band { position: absolute; left: 0; width: 100%; background: var(--orange); }
  .band--upper { top: 94px; height: 270px; }
  .band--lower { top: 460px; height: 112px; }
  .abs { position: absolute; line-height: 1; white-space: nowrap; }
  .section-title { font-size: 46px; font-weight: 600; color: var(--orange); letter-spacing: -0.5px; }
  .price { display: flex; align-items: baseline; font-weight: 600; }
  .price .size { font-size: 28px; color: var(--ink); margin-right: 6px; }
  .price .cur { font-size: 17px; color: var(--ink); margin-right: 1px; }
  .price .whole { font-size: 30px; color: var(--orange); }
  .price .cents { font-size: 18px; color: var(--orange); }
  .shot-note { font-family: "Nunito", sans-serif; font-weight: 700; font-size: 11px; color: var(--orange); }
  .item { font-size: 27px; font-weight: 600; color: var(--ink); }
  .item-list { display: flex; flex-direction: column; gap: 14px; }
  .note { font-family: "Nunito", sans-serif; font-size: 11px; font-weight: 400; color: var(--white); margin-left: 4px; }
  .extras { font-family: "Nunito", sans-serif; font-size: 15px; font-weight: 800; color: var(--white); list-style: none; line-height: 22.6px; }
  .extras li { position: relative; padding-left: 19px; }
  .extras li::before { content: "•"; position: absolute; left: 1px; }
  .extras li.plus::before { content: "+"; left: 0; }
  .extras .plain { font-weight: 400; }
  .espresso-price { font-size: 27px; font-weight: 600; color: var(--white); }
  .espresso-price small { font-size: 15px; margin-right: 6px; }
  .surcharge { font-family: "Nunito", sans-serif; font-size: 14px; font-weight: 800; color: var(--white); margin-left: 4px; }
</style>
</head>
<body>
<main class="menu-board">
  <div class="band band--upper"></div>
  <div class="band band--lower"></div>

  <!-- Coffee -->
  <h2 class="abs section-title" style="left:30px;top:36px;">Coffee</h2>
  <div class="abs price" style="left:248px;top:40px;"><span class="size">S</span><span class="cur">$</span><span class="whole">3</span><span class="cents">.80</span></div>
  <div class="abs shot-note" style="left:248px;top:70px;">(1 Shot)</div>
  <div class="abs price" style="left:350px;top:40px;"><span class="size">M</span><span class="cur">$</span><span class="whole">4</span><span class="cents">.50</span></div>
  <div class="abs shot-note" style="left:350px;top:70px;">(2 Shot)</div>
  <div class="abs price" style="left:459px;top:40px;"><span class="size">L</span><span class="cur">$</span><span class="whole">4</span><span class="cents">.90</span></div>
  <div class="abs shot-note" style="left:459px;top:70px;">(2 Shot)</div>

  <div class="abs item-list" style="left:30px;top:113px;">
    <span class="item">Espresso Shot</span>
    <span class="item">Long Black</span>
    <span class="item">Flat White</span>
    <span class="item">Latte</span>
    <span class="item">Cappuccino</span>
    <span class="item">Hot Chocolate</span>
  </div>
  <div class="abs espresso-price" style="left:282px;top:112px;"><small>$</small>2.90</div>
  <ul class="abs extras" style="left:280px;top:145px;">
    <li class="plus">50¢</li>
    <li>Soy</li>
    <li>Mocha</li>
    <li>Vienna</li>
    <li>Decaf (fresh)</li>
    <li>Syrups; <span class="plain">vanilla, caramel, hazelnut</span></li>
    <li>Cream</li>
    <li>Coffee shot</li>
    <li>White chocolate</li>
  </ul>

  <!-- Frappes -->
  <h2 class="abs section-title" style="left:604px;top:36px;">Frappes</h2>
  <div class="abs price" style="left:902px;top:42px;"><span class="size">M</span><span class="cur">$</span><span class="whole">5</span><span class="cents">.00</span></div>
  <div class="abs price" style="left:1010px;top:42px;"><span class="size">L</span><span class="cur">$</span><span class="whole">5</span><span class="cents">.50</span></div>

  <div class="abs item-list" style="left:604px;top:111px;">
    <span class="item">Vanilla</span>
    <span class="item">Hazelnut</span>
    <span class="item">Caramel</span>
    <span class="item">Chocolate</span>
    <span class="item">Coffee</span>
  </div>
  <div class="abs item" style="left:832px;top:108px;">Chai</div>
  <div class="abs item" style="left:832px;top:145px;">Iced Chocolate<span class="note">1 scoop ice cream</span></div>
  <div class="abs item" style="left:832px;top:181px;">Iced Coffee<span class="note" style="margin-left:8px;">1 scoop ice cream</span></div>
  <ul class="abs extras" style="left:832px;top:216px;">
    <li class="plus">50¢</li>
    <li>Mocha</li>
    <li>Cream</li>
    <li>Syrups; <span class="plain">vanilla, caramel, hazelnut</span></li>
  </ul>

  <!-- Fruity Frappes -->
  <h2 class="abs section-title" style="left:30px;top:396px;font-size:44px;">Fruity Frappes</h2>
  <div class="abs price" style="left:352px;top:402px;"><span class="size">M</span><span class="cur">$</span><span class="whole">5</span><span class="cents">.00</span></div>
  <div class="abs price" style="left:450px;top:402px;"><span class="size">L</span><span class="cur">$</span><span class="whole">5</span><span class="cents">.50</span></div>

  <div class="abs item-list" style="left:30px;top:478px;">
    <span class="item">Mango</span>
    <span class="item">Strawberry</span>
  </div>
  <div class="abs item-list" style="left:279px;top:478px;">
    <span class="item">Pineapple Paradise</span>
    <span class="item">Banana Smoothie<span class="surcharge">+ 50¢</span></span>
  </div>

  <!-- Chai -->
  <h2 class="abs section-title" style="left:604px;top:396px;">Chai</h2>
  <div class="abs price" style="left:820px;top:402px;"><span class="size">S</span><span class="cur">$</span><span class="whole">3</span><span class="cents">.80</span></div>
  <div class="abs price" style="left:922px;top:402px;"><span class="size">M</span><span class="cur">$</span><span class="whole">4</span><span class="cents">.50</span></div>
  <div class="abs price" style="left:1030px;top:402px;"><span class="size">L</span><span class="cur">$</span><span class="whole">4</span><span class="cents">.90</span></div>

  <div class="abs item-list" style="left:604px;top:478px;">
    <span class="item">Club Cinnamon</span>
    <span class="item">Vanilla Honey</span>
  </div>
</main>
</body>
</html>
```